Why engage Insight Harbor?

We are starting a new company that will perform usability consulting and offer usability lab rental. We are in need a one page description flyer.
Updates

Wow! We saw some very interesting and creative flyers posted for review in our contest.

Unfortunately, my schedule became a bit crazy and I may not get back to evaluating them until next week :(  In the meantime, I did want to say thank you for your entries!

Cheers!
Marla

Target Market(s)

product designers, human factors/usability researchers, consumer researcher firms, etc

Industry/Entity Type

It Company

Requirements
Must have
• We would like to see designs with a simple, yet modern, sophisticated feel. I will include our logo images that need to be incorporated along with the font used.

The file called flyer.pdf has all of the information that needs to be included.

Please include 1-3 appropriate stock photos. Please see text in flyer.pdf for description of our services.

Nice to have
• Additionally, there is a sample flyer design that we like for reference. Not a requirement...it is just a reference for the kind of style that we are looking for.

```html
<!DOCTYPE html>
<html lang="en">
<head>
<meta charset="utf-8">
<title>Insight Harbor – Usability Research Flyer</title>
<link href="https://fonts.googleapis.com/css2?family=Open+Sans:wght@400;600;700&display=swap" rel="stylesheet">
<style>
  :root {
    --navy: #1f3566;
    --navy-deep: #182b55;
    --green: #8cc63f;
    --green-text: #7bb03a;
    --panel: #e9f2da;
    --rule: #b9c9a3;
    --ink: #1e1e1e;
    --white: #ffffff;
  }
  * { box-sizing: border-box; margin: 0; padding: 0; }
  html, body { width: 927px; height: 1200px; overflow: hidden; background: var(--white); }
  body { font-family: "Open Sans", Arial, sans-serif; color: var(--ink); position: relative; }

  .hero-photo {
    position: absolute; left: 0; top: 0; width: 500px; height: 462px;
    background: radial-gradient(ellipse at 48% 60%, #c9a36a 0%, #7a5a3a 28%, #2e2a28 60%, #121212 100%);
  }

  .brand { position: absolute; left: 500px; top: 0; width: 427px; height: 170px; padding: 52px 0 0 30px; }
  .brand-name {
    display: flex; align-items: center; gap: 10px;
    font-size: 37px; font-weight: 600; color: var(--navy); letter-spacing: 0.5px; line-height: 1; white-space: nowrap;
  }
  .brand-dot { width: 20px; height: 20px; border-radius: 50%; background: var(--green); flex: none; }
  .brand-address { margin-top: 26px; font-size: 14.5px; font-weight: 700; color: var(--navy); white-space: nowrap; }

  .intro {
    position: absolute; left: 500px; top: 170px; width: 427px; height: 292px;
    background: var(--navy); color: var(--white);
    padding: 20px 60px 0 30px; font-size: 16.6px; line-height: 1.28;
  }
  .intro p + p { margin-top: 16px; }

  .why-panel {
    position: absolute; left: 48px; top: 488px; width: 838px; height: 641px;
    background: var(--panel); border-radius: 18px; overflow: hidden;
  }
  .why-tab {
    position: absolute; left: 0; top: 0; bottom: 0; width: 55px; background: var(--green);
    display: flex; align-items: center; justify-content: center;
  }
  .why-tab span {
    writing-mode: vertical-rl; transform: rotate(180deg);
    color: var(--white); font-size: 25px; font-weight: 400; letter-spacing: 1.5px; white-space: nowrap;
  }
  .features { position: absolute; left: 73px; top: 12px; right: 20px; }
  .feature { display: flex; border-bottom: 1px solid var(--rule); padding-top: 6px; }
  .feature:last-child { border-bottom: none; }
  .feature h3 { width: 159px; flex: none; font-size: 15.5px; font-weight: 600; color: var(--green-text); line-height: 1.2; }
  .feature p { font-size: 12.4px; line-height: 1.45; color: var(--ink); }

  .footer {
    position: absolute; left: 0; top: 1147px; width: 927px; height: 53px;
    background: var(--navy-deep); color: var(--white);
    display: flex; align-items: center; padding-left: 68px;
    font-size: 25px; font-weight: 700; letter-spacing: 1.5px;
  }
  .footer .phone { display: flex; align-items: center; gap: 10px; }
  .footer .web { margin-left: 72px; }
</style>
</head>
<body>
  <div class="hero-photo" role="img" aria-label="Researchers in lab coats leaning over a lit cutaway dollhouse with furnished rooms"></div>

  <header class="brand">
    <div class="brand-name"><span class="brand-dot"></span>INSIGHT HARBOR</div>
    <div class="brand-address">2140 W. Harbor Point Road, Tempe AZ 85281</div>
  </header>

  <section class="intro">
    <p>We are a network of human factors engineers, usability specialists, and cognitive/consumer psychologists, who help you design and evaluate the usefulness, usability and desirability of your products.</p>
    <p>Lease our state of the art consumer research and usability lab, or partner with us on usability testing, eyetracking studies, participatory design, online survey research, ethnographic studies, focus groups and more.</p>
  </section>

  <section class="why-panel">
    <div class="why-tab"><span>WHY ENGAGE INSIGHT HARBOR?</span></div>
    <div class="features">
      <div class="feature" style="height:94px"><h3>Experience</h3><p>Founded by a Professor of Cognitive Psychology and Human Factors with over twenty years of experience, our group includes MS and PhD level consultants with experience working for and consulting with companies like Tellavo, KQ, Orvane, Sennit, Halvor Hospitals, Merrow and Tasker, Zentrivo, and Lumovale.</p></div>
      <div class="feature" style="height:76px"><h3>Service</h3><p>Full range of consumer research and usability services, including ethnography, participatory design, questionnaires, user diaries, usability testing, usability evaluation, card sorting, psychometric scaling, focus groups and more.</p></div>
      <div class="feature" style="height:58px"><h3>Range of products and industries</h3><p>Our consultants have extensive experience in design and evaluation of computing, web, tablet, smart phone, product, medical, consumer, and many other types of products and user interfaces.</p></div>
      <div class="feature" style="height:53px"><h3>Client Service Specialist</h3><p>Need copies, printing, lunch, or dinner reservations? Our client service specialist will make sure you have everything you need.</p></div>
      <div class="feature" style="height:59px"><h3>Recruiting</h3><p>Sizable database with ability to recruit research participants according to age, sex, occupation, health status, and other parameters.</p></div>
      <div class="feature" style="height:60px"><h3>Onsite or remote streaming video</h3><p>Sessions can be viewed in many ways: Through our observation mirror, in our meeting room via pan-tilt-zoom camera, at your site on your computer, on your tablet or phone.</p></div>
      <div class="feature" style="height:35px"><h3>Audio/video</h3><p>On-site video editing. Highlight video included in facility rental.</p></div>
      <div class="feature" style="height:40px"><h3>Office space</h3><p>Meeting room for work, phone calls and conference calls. Wireless Internet.</p></div>
      <div class="feature" style="height:59px"><h3>Accessibility</h3><p>Located on the first floor, with ample, free, convenient and handicap parking. Adjustable artificial and natural lighting.</p></div>
      <div class="feature" style="height:56px"><h3>Transcription</h3><p>Transcription services and word frequency key-words-in-context, and word co-occurrence analyses available</p></div>
      <div class="feature" style="height:40px"><h3>Bilingual</h3><p>Several consultants fluent in both English and Spanish</p></div>
    </div>
  </section>

  <footer class="footer">
    <span class="phone">
      <svg width="16" height="24" viewBox="0 0 16 24" aria-hidden="true"><path d="M4 1 L7 1 L8 7 L5.5 8.5 C6 12 7.5 15 10 17 L12 15.5 L15 19 L12.5 22.5 C6 21 1 12 1.5 4 Z" fill="none" stroke="#fff" stroke-width="1.8" stroke-linejoin="round"/></svg>
      480.555.0147
    </span>
    <span class="web">WWW.INSIGHT-HARBOR.COM</span>
  </footer>
</body>
</html>
```